Brochure Design Project

We need a brochure to introduce clients who work in our local area to become a VIP clients based on the fact they work in the local area. We have call centers of major companies with 1 km of our hair salon as well as head offices of many big companies some with staff of 400 and Australia second biggest University Calvera with 1500 international student who live mins away who use our local shops to have lunch as we have many food outlets we have a wide mix of people walking past our salon at lunch time demographic ages from 19yo call center staff to CEO's. I not sure whether to use VIP what are your thoughts and statistics say (overuse). I need your thoughts on how they would qualify to become a VIP i was thinking they only need to show proof they work in one of the offices in our area to become a member I will provide them with a small plastic bar coded tag to identify themselves if they become members you can profile our business from our website www.bellomira.com.au our NEW logo is on our facebook page Bellomira Hair and Make up web logo is the old one I think we should put in our price list which is on our website i was thinking 20% off normal prices subject to change.
Updates

Target Market(s)

Local traders and local offices we have many call centre staff and big company head offices with in 1 km

Industry/Entity Type

Plastic

Requirements
Must have
• Simplicity not too busy less is more
Nice to have
• A4 Folded
Should not have
• Too much text

```html
<!DOCTYPE html>
<html lang="en">
<head>
<meta charset="utf-8">
<title>Bellomira Hair and Make up – VIP &amp; Price List</title>
<link rel="stylesheet" href="https://fonts.googleapis.com/css2?family=Questrial&family=Didact+Gothic&display=swap">
<style>
  :root {
    --page: #ffffff;
    --ink: #000000;
    --panel: #000000;
    --paper-text: #ffffff;
    --blush: #f3e1ea;
    --blush-strong: #f4dbe8;
    --photo-light: #d9d9d9;
    --photo-mid: #8a8a8a;
    --photo-dark: #2a2a2a;
  }
  * { margin: 0; padding: 0; box-sizing: border-box; }
  html, body { width: 1200px; height: 1000px; overflow: hidden; background: var(--page); }
  body { position: relative; font-family: "Questrial", "Century Gothic", sans-serif; }

  .brochure {
    position: absolute; left: 10px; top: 82px;
    width: 1178px; height: 836px;
    background: var(--panel); overflow: hidden;
  }
  .top-left-field {
    position: absolute; left: 0; top: 0; width: 400px; height: 258px;
    background: var(--page);
  }
  .photo { position: absolute; inset: 0; }
  .photo--bob {
    background: linear-gradient(150deg, var(--photo-dark) 0%, var(--photo-mid) 45%, var(--photo-light) 100%);
    clip-path: polygon(395px 0, 610px 0, 530px 258px, 360px 258px);
  }
  .photo--blonde {
    background: radial-gradient(ellipse at 45% 55%, #eeeeee 0%, #b5b5b5 45%, #4a4a4a 100%);
    clip-path: polygon(630px 0, 955px 0, 865px 258px, 535px 258px);
  }
  .photo--long-hair {
    background: linear-gradient(100deg, #e8e8e8 0%, #a9a9a9 50%, #5a5a5a 100%);
    clip-path: polygon(965px 0, 1178px 0, 1178px 258px, 870px 258px);
  }
  .photo--updo {
    background: linear-gradient(90deg, #3a3a3a 0%, #9c9c9c 40%, #d0d0d0 70%, #7a7a7a 100%);
    clip-path: polygon(0 258px, 392px 258px, 322px 836px, 0 836px);
  }

  .vip-circle {
    position: absolute; left: -15px; top: -72px;
    width: 410px; height: 410px; border-radius: 50%;
    background: var(--blush);
  }
  .vip-copy {
    position: absolute; left: 40px; top: 112px; width: 336px;
    color: var(--ink);
  }
  .vip-copy__title {
    font-family: "Didact Gothic", "Century Gothic", sans-serif;
    font-style: italic; font-weight: 400;
    font-size: 38px; line-height: 38px;
  }
  .vip-copy__text { font-size: 15.5px; line-height: 21.5px; }

  .price-list-title {
    position: absolute; left: 358px; top: 517px;
    transform: translate(-50%, -50%) rotate(-90deg);
    font-family: "Didact Gothic", "Century Gothic", sans-serif;
    font-size: 62px; letter-spacing: 1px; white-space: nowrap;
    color: var(--blush-strong);
  }

  .menu { position: absolute; color: var(--paper-text); font-size: 12.5px; }
  .menu__heading { text-transform: uppercase; font-size: 12.5px; line-height: 16px; }
  .menu__intro { font-size: 11.5px; line-height: 15px; }
  .menu__note { font-size: 11.5px; line-height: 16px; }

  .price-table { position: absolute; color: var(--paper-text); font-size: 12.5px; }
  .price-table__head, .price-table__row { display: grid; align-items: end; }
  .price-table__head { font-size: 12.5px; line-height: 15px; margin-bottom: 6px; }
  .price-table__row { line-height: 21px; }
  .price-table__title { text-transform: uppercase; align-self: center; }

  .price-table--cutting .price-table__head,
  .price-table--cutting .price-table__row { grid-template-columns: 114px 101px 100px; }
  .price-table--cutting .price-table__head { margin-bottom: 3px; }
  .price-table--styling .price-table__head,
  .price-table--styling .price-table__row { grid-template-columns: 167px 75px 80px; }
  .price-table--colouring .price-table__head,
  .price-table--colouring .price-table__row { grid-template-columns: 164px 76px 80px; }
  .price-table--right .price-table__head,
  .price-table--right .price-table__row { grid-template-columns: 163px 77px 80px; }
</style>
</head>
<body>
  <main class="brochure">
    <div class="top-left-field"></div>
    <div class="photo photo--bob" role="img" aria-label="Black and white portrait of a model with a tousled bob"></div>
    <div class="photo photo--blonde" role="img" aria-label="Black and white close-up of a model with windswept blonde hair"></div>
    <div class="photo photo--long-hair" role="img" aria-label="Black and white portrait of a model with long straight blonde hair and bangles"></div>
    <div class="photo photo--updo" role="img" aria-label="Black and white profile of a model having a sleek high ponytail styled"></div>

    <div class="vip-circle"></div>
  </main>

  <section class="vip-copy">
    <h1 class="vip-copy__title">VIP</h1>
    <p class="vip-copy__text">VIP Clients will get 15% discount on all services (excludes retail purchases) with an additional 5% if you visit Monday to Friday before 4.00pm. All VIP clients are automatically included in our loyalty program and earn extra discounts towards hair services. If you work in the local area of Mount Ardene (within a 1km range) you could become a VIP today!</p>
  </section>

  <h2 class="price-list-title">PRICE LIST</h2>

  <section class="menu" style="left:453px; top:356px; width:330px;">
    <h3 class="menu__heading">Cuts</h3>
    <p class="menu__intro">Every consultation gives careful consideration examining face shapes, features and contours. Precise intensive analysis is a reflection of our extensive in-house educational programme.</p>
  </section>

  <div class="price-table price-table--cutting" style="left:455px; top:433px;">
    <div class="price-table__head"><span class="price-table__title">Cutting</span><span>Style Director</span><span>Principal Stylist</span></div>
    <div class="price-table__row"><span>Ladies’ Style Cut*</span><span>$80.00</span><span>$70.00</span></div>
    <div class="price-table__row"><span>Mens’ Style Cut*</span><span>$55.00</span><span>$45.00</span></div>
  </div>
  <p class="menu menu__note" style="left:455px; top:496px;">*Salon Director- from $90.00 (Ladies) and from $65.00 (men)</p>

  <div class="price-table price-table--styling" style="left:455px; top:528px;">
    <div class="price-table__head"><span class="price-table__title">Blow Wave/Styling</span><span>Style<br>Director</span><span>Principal<br>Stylist</span></div>
    <div class="price-table__row"><span>Short</span><span>$50.00</span><span>$40.00</span></div>
    <div class="price-table__row"><span>Medium</span><span>$60.00</span><span>$50.00</span></div>
    <div class="price-table__row"><span>Long</span><span>$70.00</span><span>$60.00</span></div>
  </div>

  <section class="menu" style="left:453px; top:634px; width:300px;">
    <h3 class="menu__heading">Colours</h3>
    <p class="menu__intro">Colour consultations explore a client’s eye colour, skin tone, wants, needs and lifestyle . We offer directional advice, believing it is paramount in stimulating creativity for new ideas or for the refreshment of existing colour.</p>
  </section>

  <div class="price-table price-table--colouring" style="left:455px; top:726px;">
    <div class="price-table__head"><span class="price-table__title">Colouring</span><span>Technical<br>Director</span><span>Principal<br>Colourist</span></div>
    <div class="price-table__row"><span>Regrowth</span><span>$80.00</span><span>$65.00</span></div>
    <div class="price-table__row"><span>Short</span><span>$80.00</span><span>$70.00</span></div>
    <div class="price-table__row"><span>Medium</span><span>$90.00</span><span>$80.00</span></div>
    <div class="price-table__row"><span>Long</span><span>$100.00</span><span>$90.00</span></div>
  </div>

  <div class="price-table price-table--right" style="left:850px; top:362px;">
    <div class="price-table__head"><span class="price-table__title">PURA (Ammonia Free)</span><span>Technical<br>Director</span><span>Principal<br>Colourist</span></div>
    <div class="price-table__row"><span>Regrowth</span><span>$85.00</span><span>$75.00</span></div>
    <div class="price-table__row"><span>Short</span><span>$90.00</span><span>$80.00</span></div>
    <div class="price-table__row"><span>Medium</span><span>$100.00</span><span>$95.00</span></div>
    <div class="price-table__row"><span>Long</span><span>$110.00</span><span>$110.00</span></div>
  </div>

  <div class="price-table price-table--right" style="left:850px; top:493px;">
    <div class="price-table__head"><span class="price-table__title">Foiling</span><span>Technical<br>Director</span><span>Principal<br>Colourist</span></div>
    <div class="price-table__row"><span>½ Head</span><span>$110.00</span><span>$85.00</span></div>
    <div class="price-table__row"><span>Full Head</span><span>$170.00</span><span>$145.00</span></div>
    <div class="price-table__row"><span>Toner</span><span>$15.00</span><span>$10.00</span></div>
  </div>

  <div class="price-table price-table--right" style="left:850px; top:605px;">
    <div class="price-table__head"><span class="price-table__title">Foils &amp; Colour</span><span>Technical<br>Director</span><span>Principal<br>Colourist</span></div>
    <div class="price-table__row"><span>Short</span><span>$125.00</span><span>$125.00</span></div>
    <div class="price-table__row"><span>Medium</span><span>$135.00</span><span>$130.00</span></div>
    <div class="price-table__row"><span>Long</span><span>$145.00</span><span>$140.00</span></div>
    <div class="price-table__row"><span>Toner</span><span>$15.00</span><span>$10.00</span></div>
  </div>

  <div class="price-table price-table--right" style="left:850px; top:735px;">
    <div class="price-table__head"><span class="price-table__title">PURA (Ammonia Free)</span><span>Technical<br>Director</span><span>Principal<br>Colourist</span></div>
    <div class="price-table__row"><span>Medium</span><span>$160.00</span><span>$145.00</span></div>
    <div class="price-table__row"><span>Long</span><span>$170.00</span><span>$160.00</span></div>
    <div class="price-table__row"><span>Toner</span><span>$15.00</span><span>$10.00</span></div>
  </div>
</body>
</html>
```